Business Card Design

Take existing logo/brand and develop business card for sales team.
We have two separate brands and require a business card for each.

1. VoxHarbor
2. MyNimbusLinko

Refer to our websites www.voxharbor.example.au and www.mynimbuslinko.example.au for designs currently implemented and in the marketplace.

Both cards are brands of our parent company Quorra Systems Pty Ltd - an Australian Telecommunications company in the medium business sector. We have only business customers, no retail/residential consumers.

Target Market(s)

Australian Business - small to medium enterprise

Industry/Entity Type

Business

Contact Information for Business Card

Lev Dorrit
Sales Director
Mobile: +61 400 555 187
Direct: +61 3 9555 0137
Email: lev@voxharbor.example.au
VoxHarbor (a brand of Quorra Systems Pty Ltd)

Lev Dorrit
Sales Director
Mobile: +61 400 555 187
Direct: +61 3 9555 0137
Email: lev@mynimbuslinko.example.au
MyNimbusLinko (a brand of Quorra Systems Pty Ltd)

Font styles to use
Sans Serif
Other font styles liked:
• Roboto Condensed, Open Sans

Requirements
Must have
• Clean lines, crisp fonts - suggest Roboto Condensed or similar.
• Must be easy to read and clear.
• Brand colour #0C8CCD
• Two colour maximum
Nice to have
• Modern, intellectual and unique design.
Should not have
• No die cuts
• No copies or rip-offs of other designs

```html
<!DOCTYPE html>
<html lang="en">
<head>
<meta charset="utf-8">
<title>Business Cards – MyNimbusLinko &amp; VoxHarbor</title>
<link rel="stylesheet" href="https://fonts.googleapis.com/css2?family=Roboto+Condensed:wght@300;400;700&display=swap">
<style>
  :root {
    --brand: #0c8ccd;
    --paper: #ffffff;
    --ink: #2e2e2e;
    --muted: #7a7a7a;
    --backdrop: #e8eaec;
  }
  * { box-sizing: border-box; margin: 0; padding: 0; }
  html, body {
    width: 720px; height: 1200px; overflow: hidden;
    background: var(--backdrop);
    font-family: "Roboto Condensed", sans-serif;
  }
  .sheet { position: relative; width: 720px; height: 1200px; }
  .card {
    position: absolute; left: 140px; width: 440px; height: 256px;
    overflow: hidden; background: var(--paper);
    box-shadow: 0 2px 6px rgba(0,0,0,.12);
  }
  .card--blue { background: var(--brand); }
  .card-1 { top: 35px; }
  .card-2 { top: 326px; }
  .card-3 { top: 617px; }
  .card-4 { top: 908px; }

  .brand { position: absolute; display: flex; align-items: center; gap: 10px; }
  .brand-name { font-weight: 400; line-height: 1; white-space: nowrap; }
  .brand-square { display: block; }
  .brand-circle { display: block; border-radius: 50%; }
  .tagline { position: absolute; font-size: 9.5px; color: var(--muted); white-space: nowrap; }

  /* MyNimbusLinko front */
  .nimbus-front .brand { left: 88px; top: 106px; }
  .nimbus-front .brand-square { width: 44px; height: 44px; background: var(--paper); }
  .nimbus-front .brand-name { font-size: 34px; color: var(--paper); }

  /* MyNimbusLinko back */
  .nimbus-back .column { position: absolute; left: 250px; top: 0; width: 190px; height: 256px; background: var(--brand); }
  .nimbus-back .person { position: absolute; left: 250px; top: 26px; width: 190px; text-align: center; color: var(--paper); }
  .nimbus-back .person-name { font-size: 16px; font-weight: 700; }
  .nimbus-back .person-title { font-size: 11px; font-weight: 300; margin-top: 2px; }
  .nimbus-back .band { position: absolute; left: 250px; width: 190px; height: 28px; background: var(--paper);
    display: flex; align-items: center; justify-content: center; font-size: 11px; color: var(--ink); white-space: nowrap; }
  .nimbus-back .rule { position: absolute; left: 214px; width: 226px; height: 8px; background: var(--brand); }
  .nimbus-back .brand { left: 24px; top: 196px; gap: 6px; }
  .nimbus-back .brand-square { width: 26px; height: 26px; background: var(--brand); }
  .nimbus-back .brand-name { font-size: 22px; color: var(--ink); }
  .nimbus-back .tagline { left: 56px; top: 224px; }

  /* VoxHarbor front */
  .vox-front .arc { position: absolute; right: -70px; top: -130px; width: 240px; height: 240px; border-radius: 50%; background: var(--paper); }
  .vox-front .brand { left: 40px; top: 112px; }
  .vox-front .brand-circle { width: 36px; height: 36px; background: var(--paper); }
  .vox-front .brand-name { font-size: 32px; font-weight: 300; color: var(--paper); }

  /* VoxHarbor back */
  .vox-back .arc { position: absolute; left: 20px; top: -140px; width: 210px; height: 210px; border-radius: 50%; background: var(--brand); }
  .vox-back .brand { left: 28px; top: 128px; }
  .vox-back .brand-circle { width: 34px; height: 34px; background: var(--brand); }
  .vox-back .brand-name { font-size: 32px; font-weight: 300; color: var(--brand); }
  .vox-back .tagline { left: 56px; top: 170px; }
  .vox-back .person { position: absolute; left: 272px; top: 128px; text-align: center; width: 130px; }
  .vox-back .person-name { font-size: 15px; font-weight: 700; color: var(--brand); }
  .vox-back .person-title { font-size: 11px; color: var(--ink); }
  .vox-back .contacts { position: absolute; right: 24px; top: 180px; text-align: right; font-size: 10.5px; line-height: 16px; color: var(--ink); }
  .vox-back .tab { position: absolute; right: 0; top: 186px; width: 6px; height: 20px; background: var(--brand); }
</style>
</head>
<body>
<main class="sheet">

  <section class="card card--blue card-1 nimbus-front" aria-label="MyNimbusLinko card front">
    <div class="brand">
      <span class="brand-square"></span>
      <span class="brand-name">MyNimbusLinko</span>
    </div>
  </section>

  <section class="card card-2 nimbus-back" aria-label="MyNimbusLinko card back">
    <div class="column"></div>
    <div class="person">
      <p class="person-name">Lev Dorrit</p>
      <p class="person-title">Sales Director</p>
    </div>
    <div class="rule" style="top:78px"></div>
    <div class="band" style="top:86px">m : +61 400 555 187</div>
    <div class="rule" style="top:114px"></div>
    <div class="band" style="top:122px">d : +61 3 9555 0137</div>
    <div class="rule" style="top:150px"></div>
    <div class="band" style="top:158px">e : lev@mynimbuslinko.example.au</div>
    <div class="rule" style="top:186px"></div>
    <div class="brand">
      <span class="brand-square"></span>
      <span class="brand-name">MyNimbusLinko</span>
    </div>
    <p class="tagline">a brand of Quorra Systems Pty Ltd</p>
  </section>

  <section class="card card--blue card-3 vox-front" aria-label="VoxHarbor card front">
    <div class="arc"></div>
    <div class="brand">
      <span class="brand-circle"></span>
      <span class="brand-name">VoxHarbor</span>
    </div>
  </section>

  <section class="card card-4 vox-back" aria-label="VoxHarbor card back">
    <div class="arc"></div>
    <div class="brand">
      <span class="brand-circle"></span>
      <span class="brand-name">VoxHarbor</span>
    </div>
    <p class="tagline">a brand of Quorra Systems Pty Ltd</p>
    <div class="person">
      <p class="person-name">Lev Dorrit</p>
      <p class="person-title">Sales Director</p>
    </div>
    <div class="contacts">
      <p>m : +61 400 555 187</p>
      <p>d : +61 3 9555 0137</p>
      <p>e : lev@voxharbor.example.au</p>
    </div>
    <div class="tab"></div>
  </section>

</main>
</body>
</html>
```